Use responsive design to make this page look and behave awesome in any size

YOU CAN SUBMIT PSD, HOWEVER, THE WINNER MUST SUBMIT PROVIDE A SINGLE CODED PAGE PER THE LINK AND INSTRUCTIONS AT THE BOTTOM OF THIS BRIEF. While developing an internal website, we realized we are not super great at making things look awesome and responsive for phone/tablet/desktop. Thats where you come in. We want you to take this code, Fork it, and then make it look awesome and work great on any size device.

Task at hand:

This page is a simple dashboard showing how a number of stores stack up against each other and against a corporate goal.

Top: Goal title, and where the logged in person's store stands in the ranking.
Green means you are in compliance
Red means you are not in compliance

Middle: Description of goal. Words to describe what the corporate goal is, and a target number.

Bottom: Here we just want to show the top 10 and bottom 5 out of 100+ stores. if your in the top ten, you are highlighted. If your in the bottom 5, you will be highlighted there too. If you are in the middle, we would put the your store info between the top and bottom... indicating your in the middle.
Green means you they are in compliance
Red means they are not in compliance

Your Mission is not only to make this look fantastic and responsive, but to have usable code in there.

You don't need to do any logic. All we care about is look and feel and responsive behavior on different size browsers.

The winner obviously gets the prize, and hopefully can become a solid resource to do more of this type of thing for us in the future.

Instructions:
Go to this link: https://codewharf.example/edit/tpl-tallyboard-widget
Click on the blue Fork button. This will give you a new URL that you can paste back into the contest to review results for us to see your work.
Uploading pictures is not necessary as the responsive code is what is important here.

Good luck!

Number of Pages Required

1 page

Requirements
Must have
• The page must be responsive and look very professional AND game like.
Should not have
• plugins. just native code

```html
<!DOCTYPE html>
<html lang="en">
<head>
<meta charset="utf-8">
<title>Tallyboard – Store Goal Dashboard</title>
<link rel="stylesheet" href="https://fonts.googleapis.com/css2?family=Roboto:wght@400;500;700&display=swap">
<style>
:root{
  --canvas:#ffffff;
  --panel:#dcdcdc;
  --card:#ffffff;
  --ink:#333333;
  --muted:#555555;
  --good:#1ea83c;
  --bad:#e53935;
  --stripe:#dcf1f8;
  --goal-bg:#e8e8e8;
  --highlight:#e31e24;
  --icon-fill:#d7e8dc;
  --row-h:21px;
  --group-gap:24px;
}
*{box-sizing:border-box;margin:0;padding:0}
html,body{width:1200px;height:2885px;overflow:hidden}
body{background:var(--canvas);font-family:'Roboto',Arial,sans-serif;color:var(--ink);position:relative}
.view-label{position:absolute;font-size:14px;color:var(--ink);transform:translateX(-50%);white-space:nowrap}
.view{position:absolute}
.view--mobile{left:145px;top:145px;width:277px;border:10px solid var(--panel);background:var(--card);padding-bottom:8px}
.view--mobile .card + .card{margin-top:34px}
.view--tablet{left:503px;top:145px;width:662px;height:1070px;background:var(--panel);padding:20px 0 0 50px;display:grid;grid-template-columns:273px 273px;column-gap:16px;row-gap:20px;align-content:start}
.view--desktop{left:15px;top:2300px;width:1170px;height:575px;background:var(--panel);padding:20px 0 0 28px;display:grid;grid-template-columns:repeat(4,262px);column-gap:22px;align-items:start;--row-h:18px;--group-gap:40px}
.view--desktop .card{height:535px}
.card{background:var(--card);padding:14px 6px 16px}
.card-head{display:flex;align-items:center;height:62px;padding-left:10px}
.card-icon{width:42px;height:42px;border-radius:8px;background:var(--icon-fill);flex:none}
.card-titles{margin-left:18px}
.card-title{font-size:21px;font-weight:700;color:var(--ink);line-height:1.1}
.card-result{font-size:15px;color:var(--ink);margin-top:2px}
.card-result strong{color:var(--good);font-size:19px;font-weight:700;margin-left:6px}
.goal{display:grid;grid-template-columns:1fr 62px;align-items:center;background:var(--goal-bg);padding:4px 6px;margin:4px 0 6px;font-size:12.5px;line-height:1.35;color:var(--muted)}
.goal-target{font-size:16px;text-align:center;color:var(--ink)}
.ranking{list-style:none}
.ranking + .ranking{margin-top:var(--group-gap)}
.row{display:grid;grid-template-columns:34px 1fr 54px;align-items:center;height:var(--row-h);padding:0 6px;font-size:11.5px}
.row:nth-child(even){background:var(--stripe)}
.rank{color:var(--muted)}
.row.good .store,.row.good .score{color:var(--good)}
.row.bad .store,.row.bad .score{color:var(--bad)}
.row.you{background:var(--highlight)}
.row.you span{color:#fff!important;font-weight:500}
</style>
</head>
<body>

<p class="view-label" style="left:283px;top:82px">Mobile View (320 px in width)</p>
<p class="view-label" style="left:834px;top:82px">Tablet View (768 px in width)</p>
<p class="view-label" style="left:600px;top:2246px">Desktop View (1366 px in width)</p>

<!-- ===== Mobile ===== -->
<main class="view view--mobile">
  <section class="card">
    <header class="card-head"><div class="card-icon" role="img" aria-label="Team goal icon"></div><div class="card-titles"><h2 class="card-title">Team</h2><p class="card-result">Your result: <strong>92.1 %</strong></p></div></header>
    <div class="goal"><span>Use Slow Stock wherever possible</span><span class="goal-target">80 %</span></div>
    <ol class="ranking">
      <li class="row bad"><span class="rank">1</span><span class="store">(1) yjcQbtCyQu</span><span class="score">1 %</span></li>
      <li class="row bad"><span class="rank">2</span><span class="store">(1) crsmicfXwS</span><span class="score">1 %</span></li>
      <li class="row bad"><span class="rank">3</span><span class="store">(2) wnLJojLRSf</span><span class="score">2 %</span></li>
      <li class="row bad"><span class="rank">4</span><span class="store">(2) swEbjeRrpi</span><span class="score">2 %</span></li>
      <li class="row bad"><span class="rank">5</span><span class="store">(4) oUauMPncOA</span><span class="score">4 %</span></li>
      <li class="row bad"><span class="rank">6</span><span class="store">(5) vYuFdHZExR</span><span class="score">5 %</span></li>
      <li class="row bad"><span class="rank">7</span><span class="store">(5) jvBnNaGkeE</span><span class="score">5 %</span></li>
      <li class="row bad"><span class="rank">8</span><span class="store">(6) CuWIivexCs</span><span class="score">6 %</span></li>
      <li class="row bad"><span class="rank">9</span><span class="store">(7) XQFCUbSoko</span><span class="score">7 %</span></li>
      <li class="row bad"><span class="rank">10</span><span class="store">(7) GucpFDVVJP</span><span class="score">7 %</span></li>
    </ol>
    <ol class="ranking">
      <li class="row good"><span class="rank">96</span><span class="store">(94) VaDGNkvwai</span><span class="score">94 %</span></li>
      <li class="row good"><span class="rank">97</span><span class="store">(94) IBjPTiBSlh</span><span class="score">94 %</span></li>
      <li class="row good"><span class="rank">98</span><span class="store">(96) iWwFhTvkZb</span><span class="score">96 %</span></li>
      <li class="row good"><span class="rank">99</span><span class="store">(96) IzLCIRKlLu</span><span class="score">96 %</span></li>
      <li class="row good"><span class="rank">100</span><span class="store">(96) pXPrzpcrUY</span><span class="score">96 %</span></li>
    </ol>
  </section>
  <section class="card">
    <header class="card-head"><div class="card-icon" role="img" aria-label="Slow stock goal icon"></div><div class="card-titles"><h2 class="card-title">Slow</h2><p class="card-result">Your result: <strong>0 %</strong></p></div></header>
    <div class="goal"><span>Less than 0% of inventory slower than 100 days</span><span class="goal-target">&lt; 1 %</span></div>
    <ol class="ranking">
      <li class="row good"><span class="rank">1</span><span class="store">(89) NZBGVulmnc</span><span class="score">0 %</span></li>
      <li class="row good"><span class="rank">2</span><span class="store">(80) GaccDehKUO</span><span class="score">0 %</span></li>
      <li class="row good"><span class="rank">3</span><span class="store">(55) aPfpNcqcDh</span><span class="score">0 %</span></li>
      <li class="row good"><span class="rank">4</span><span class="store">(97) YqyVfKITII</span><span class="score">0 %</span></li>
      <li class="row good"><span class="rank">5</span><span class="store">(67) PvQdqyeaHr</span><span class="score">0 %</span></li>
      <li class="row bad you"><span class="rank">6</span><span class="store">(00) Your Store</span><span class="score">2 %</span></li>
      <li class="row bad"><span class="rank">7</span><span class="store">(40) jyMfVYIVbl</span><span class="score">2 %</span></li>
      <li class="row bad"><span class="rank">8</span><span class="store">(11) QSESmpDJqw</span><span class="score">2 %</span></li>
      <li class="row bad"><span class="rank">9</span><span class="store">(71) nIlaXFpJWv</span><span class="score">2 %</span></li>
      <li class="row bad"><span class="rank">10</span><span class="store">(51) ENrkkveKpb</span><span class="score">2 %</span></li>
    </ol>
    <ol class="ranking">
      <li class="row bad"><span class="rank">96</span><span class="store">(90) VZgTUWgJTU</span><span class="score">8 %</span></li>
      <li class="row bad"><span class="rank">97</span><span class="store">(67) nRGVsKcZhP</span><span class="score">9 %</span></li>
      <li class="row bad"><span class="rank">98</span><span class="store">(32) JckeFPUVJV</span><span class="score">9 %</span></li>
      <li class="row bad"><span class="rank">99</span><span class="store">(57) RxygcFNCRC</span><span class="score">9 %</span></li>
      <li class="row bad"><span class="rank">100</span><span class="store">(20) MmydxeaOMu</span><span class="score">10 %</span></li>
    </ol>
  </section>
  <section class="card">
    <header class="card-head"><div class="card-icon" role="img" aria-label="Inventory turns goal icon"></div><div class="card-titles"><h2 class="card-title">Turns</h2><p class="card-result">Your result: <strong>2.2</strong></p></div></header>
    <div class="goal"><span>Turn inventory 6 or more times a year</span><span class="goal-target">&lt; 6</span></div>
    <ol class="ranking">
      <li class="row bad"><span class="rank">1</span><span class="store">(8) VZaEOSVkef</span><span class="score">0.2</span></li>
      <li class="row bad"><span class="rank">2</span><span class="store">(3) PcVKNpUNmj</span><span class="score">0.2</span></li>
      <li class="row bad"><span class="rank">3</span><span class="store">(4) RIlyRZsTln</span><span class="score">0.4</span></li>
      <li class="row bad"><span class="rank">4</span><span class="store">(9) epiNQFtERO</span><span class="score">0.6</span></li>
      <li class="row bad"><span class="rank">5</span><span class="store">(3) FbFOzkjSpF</span><span class="score">0.7</span></li>
      <li class="row bad"><span class="rank">6</span><span class="store">(7) RdzzkcVqtC</span><span class="score">0.8</span></li>
      <li class="row bad"><span class="rank">7</span><span class="store">(1) DiiIXiGkTx</span><span class="score">0.8</span></li>
      <li class="row bad"><span class="rank">8</span><span class="store">(1) jxWbwORyVa</span><span class="score">0.8</span></li>
      <li class="row bad"><span class="rank">9</span><span class="store">(4) UyzYfIIMzU</span><span class="score">0.8</span></li>
      <li class="row bad"><span class="rank">10</span><span class="store">(4) KVIgJQBgAc</span><span class="score">1</span></li>
    </ol>
    <ol class="ranking">
      <li class="row good"><span class="rank">96</span><span class="store">(5) gBeGhPqZNF</span><span class="score">9.7</span></li>
      <li class="row good"><span class="rank">97</span><span class="store">(8) gGhhZFICHP</span><span class="score">9.7</span></li>
      <li class="row good"><span class="rank">98</span><span class="store">(9) emavLKfhzN</span><span class="score">9.8</span></li>
      <li class="row good"><span class="rank">99</span><span class="store">(7) PyuviZHBxH</span><span class="score">9.8</span></li>
      <li class="row good"><span class="rank">100</span><span class="store">(5) LldsyctcWm</span><span class="score">9.9</span></li>
    </ol>
  </section>
  <section class="card">
    <header class="card-head"><div class="card-icon" role="img" aria-label="Inventory value goal icon"></div><div class="card-titles"><h2 class="card-title">Values</h2><p class="card-result">Your result: <strong>1.9</strong></p></div></header>
    <div class="goal"><span>Inventory Value to be around 1.25 x you last months INVENTORY sales</span><span class="goal-target">1.25</span></div>
    <ol class="ranking">
      <li class="row good"><span class="rank">1</span><span class="store">(8) VZaEOSVkef</span><span class="score">0.2</span></li>
      <li class="row good"><span class="rank">2</span><span class="store">(3) PcVKNpUNmj</span><span class="score">0.2</span></li>
      <li class="row good"><span class="rank">3</span><span class="store">(4) RIlyRZsTln</span><span class="score">0.4</span></li>
      <li class="row good"><span class="rank">4</span><span class="store">(9) epiNQFtERO</span><span class="score">0.6</span></li>
      <li class="row good"><span class="rank">5</span><span class="store">(3) FbFOzkjSpF</span><span class="score">0.7</span></li>
      <li class="row good"><span class="rank">6</span><span class="store">(7) RdzzkcVqtC</span><span class="score">0.8</span></li>
      <li class="row good"><span class="rank">7</span><span class="store">(1) DiiIXiGkTx</span><span class="score">0.8</span></li>
      <li class="row good"><span class="rank">8</span><span class="store">(1) jxWbwORyVa</span><span class="score">0.8</span></li>
      <li class="row good"><span class="rank">9</span><span class="store">(4) UyzYfIIMzU</span><span class="score">0.8</span></li>
      <li class="row good"><span class="rank">10</span><span class="store">(7) SCXulMdjcB</span><span class="score">1</span></li>
    </ol>
    <ol class="ranking">
      <li class="row bad"><span class="rank">96</span><span class="store">(5) gBeGhPqZNF</span><span class="score">9.7</span></li>
      <li class="row bad"><span class="rank">97</span><span class="store">(8) gGhhZFICHP</span><span class="score">9.7</span></li>
      <li class="row bad"><span class="rank">98</span><span class="store">(9) emavLKfhzN</span><span class="score">9.8</span></li>
      <li class="row bad"><span class="rank">99</span><span class="store">(7) PyuviZHBxH</span><span class="score">9.8</span></li>
      <li class="row bad"><span class="rank">100</span><span class="store">(5) LldsyctcWm</span><span class="score">9.9</span></li>
    </ol>
  </section>
</main>

<!-- ===== Tablet ===== -->
<main class="view view--tablet">
  <section class="card">
    <header class="card-head"><div class="card-icon" role="img" aria-label="Team goal icon"></div><div class="card-titles"><h2 class="card-title">Team</h2><p class="card-result">Your result: <strong>92.1 %</strong></p></div></header>
    <div class="goal"><span>Use Slow Stock wherever possible</span><span class="goal-target">80 %</span></div>
    <ol class="ranking">
      <li class="row bad"><span class="rank">1</span><span class="store">(1) yjcQbtCyQu</span><span class="score">1 %</span></li>
      <li class="row bad"><span class="rank">2</span><span class="store">(1) crsmicfXwS</span><span class="score">1 %</span></li>
      <li class="row bad"><span class="rank">3</span><span class="store">(2) wnLJojLRSf</span><span class="score">2 %</span></li>
      <li class="row bad"><span class="rank">4</span><span class="store">(2) swEbjeRrpi</span><span class="score">2 %</span></li>
      <li class="row bad"><span class="rank">5</span><span class="store">(4) oUauMPncOA</span><span class="score">4 %</span></li>
      <li class="row bad"><span class="rank">6</span><span class="store">(5) vYuFdHZExR</span><span class="score">5 %</span></li>
      <li class="row bad"><span class="rank">7</span><span class="store">(5) jvBnNaGkeE</span><span class="score">5 %</span></li>
      <li class="row bad"><span class="rank">8</span><span class="store">(6) CuWIivexCs</span><span class="score">6 %</span></li>
      <li class="row bad"><span class="rank">9</span><span class="store">(7) XQFCUbSoko</span><span class="score">7 %</span></li>
      <li class="row bad"><span class="rank">10</span><span class="store">(7) GucpFDVVJP</span><span class="score">7 %</span></li>
    </ol>
    <ol class="ranking">
      <li class="row good"><span class="rank">96</span><span class="store">(94) VaDGNkvwai</span><span class="score">94 %</span></li>
      <li class="row good"><span class="rank">97</span><span class="store">(94) IBjPTiBSlh</span><span class="score">94 %</span></li>
      <li class="row good"><span class="rank">98</span><span class="store">(96) iWwFhTvkZb</span><span class="score">96 %</span></li>
      <li class="row good"><span class="rank">99</span><span class="store">(96) IzLCIRKlLu</span><span class="score">96 %</span></li>
      <li class="row good"><span class="rank">100</span><span class="store">(96) pXPrzpcrUY</span><span class="score">96 %</span></li>
    </ol>
  </section>
  <section class="card">
    <header class="card-head"><div class="card-icon" role="img" aria-label="Slow stock goal icon"></div><div class="card-titles"><h2 class="card-title">Slow</h2><p class="card-result">Your result: <strong>0 %</strong></p></div></header>
    <div class="goal"><span>Less than 0% of inventory slower than 100 days</span><span class="goal-target">&lt; 1 %</span></div>
    <ol class="ranking">
      <li class="row good"><span class="rank">1</span><span class="store">(89) NZBGVulmnc</span><span class="score">0 %</span></li>
      <li class="row good"><span class="rank">2</span><span class="store">(80) GaccDehKUO</span><span class="score">0 %</span></li>
      <li class="row good"><span class="rank">3</span><span class="store">(55) aPfpNcqcDh</span><span class="score">0 %</span></li>
      <li class="row good"><span class="rank">4</span><span class="store">(97) YqyVfKITII</span><span class="score">0 %</span></li>
      <li class="row good"><span class="rank">5</span><span class="store">(67) PvQdqyeaHr</span><span class="score">0 %</span></li>
      <li class="row bad you"><span class="rank">6</span><span class="store">(00) Your Store</span><span class="score">2 %</span></li>
      <li class="row bad"><span class="rank">7</span><span class="store">(40) jyMfVYIVbl</span><span class="score">2 %</span></li>
      <li class="row bad"><span class="rank">8</span><span class="store">(11) QSESmpDJqw</span><span class="score">2 %</span></li>
      <li class="row bad"><span class="rank">9</span><span class="store">(71) nIlaXFpJWv</span><span class="score">2 %</span></li>
      <li class="row bad"><span class="rank">10</span><span class="store">(51) ENrkkveKpb</span><span class="score">2 %</span></li>
    </ol>
    <ol class="ranking">
      <li class="row bad"><span class="rank">96</span><span class="store">(90) VZgTUWgJTU</span><span class="score">8 %</span></li>
      <li class="row bad"><span class="rank">97</span><span class="store">(67) nRGVsKcZhP</span><span class="score">9 %</span></li>
      <li class="row bad"><span class="rank">98</span><span class="store">(32) JckeFPUVJV</span><span class="score">9 %</span></li>
      <li class="row bad"><span class="rank">99</span><span class="store">(57) RxygcFNCRC</span><span class="score">9 %</span></li>
      <li class="row bad"><span class="rank">100</span><span class="store">(20) MmydxeaOMu</span><span class="score">10 %</span></li>
    </ol>
  </section>
  <section class="card">
    <header class="card-head"><div class="card-icon" role="img" aria-label="Inventory turns goal icon"></div><div class="card-titles"><h2 class="card-title">Turns</h2><p class="card-result">Your result: <strong>2.2</strong></p></div></header>
    <div class="goal"><span>Turn inventory 6 or more times a year</span><span class="goal-target">&lt; 6</span></div>
    <ol class="ranking">
      <li class="row bad"><span class="rank">1</span><span class="store">(8) VZaEOSVkef</span><span class="score">0.2</span></li>
      <li class="row bad"><span class="rank">2</span><span class="store">(3) PcVKNpUNmj</span><span class="score">0.2</span></li>
      <li class="row bad"><span class="rank">3</span><span class="store">(4) RIlyRZsTln</span><span class="score">0.4</span></li>
      <li class="row bad"><span class="rank">4</span><span class="store">(9) epiNQFtERO</span><span class="score">0.6</span></li>
      <li class="row bad"><span class="rank">5</span><span class="store">(3) FbFOzkjSpF</span><span class="score">0.7</span></li>
      <li class="row bad"><span class="rank">6</span><span class="store">(7) RdzzkcVqtC</span><span class="score">0.8</span></li>
      <li class="row bad"><span class="rank">7</span><span class="store">(1) DiiIXiGkTx</span><span class="score">0.8</span></li>
      <li class="row bad"><span class="rank">8</span><span class="store">(1) jxWbwORyVa</span><span class="score">0.8</span></li>
      <li class="row bad"><span class="rank">9</span><span class="store">(4) UyzYfIIMzU</span><span class="score">0.8</span></li>
      <li class="row bad"><span class="rank">10</span><span class="store">(4) KVIgJQBgAc</span><span class="score">1</span></li>
    </ol>
    <ol class="ranking">
      <li class="row good"><span class="rank">96</span><span class="store">(5) gBeGhPqZNF</span><span class="score">9.7</span></li>
      <li class="row good"><span class="rank">97</span><span class="store">(8) gGhhZFICHP</span><span class="score">9.7</span></li>
      <li class="row good"><span class="rank">98</span><span class="store">(9) emavLKfhzN</span><span class="score">9.8</span></li>
      <li class="row good"><span class="rank">99</span><span class="store">(7) PyuviZHBxH</span><span class="score">9.8</span></li>
      <li class="row good"><span class="rank">100</span><span class="store">(5) LldsyctcWm</span><span class="score">9.9</span></li>
    </ol>
  </section>
  <section class="card">
    <header class="card-head"><div class="card-icon" role="img" aria-label="Inventory value goal icon"></div><div class="card-titles"><h2 class="card-title">Values</h2><p class="card-result">Your result: <strong>1.9</strong></p></div></header>
    <div class="goal"><span>Inventory Value to be around 1.25 x you last months INVENTORY sales</span><span class="goal-target">1.25</span></div>
    <ol class="ranking">
      <li class="row good"><span class="rank">1</span><span class="store">(8) VZaEOSVkef</span><span class="score">0.2</span></li>
      <li class="row good"><span class="rank">2</span><span class="store">(3) PcVKNpUNmj</span><span class="score">0.2</span></li>
      <li class="row good"><span class="rank">3</span><span class="store">(4) RIlyRZsTln</span><span class="score">0.4</span></li>
      <li class="row good"><span class="rank">4</span><span class="store">(9) epiNQFtERO</span><span class="score">0.6</span></li>
      <li class="row good"><span class="rank">5</span><span class="store">(3) FbFOzkjSpF</span><span class="score">0.7</span></li>
      <li class="row good"><span class="rank">6</span><span class="store">(7) RdzzkcVqtC</span><span class="score">0.8</span></li>
      <li class="row good"><span class="rank">7</span><span class="store">(1) DiiIXiGkTx</span><span class="score">0.8</span></li>
      <li class="row good"><span class="rank">8</span><span class="store">(1) jxWbwORyVa</span><span class="score">0.8</span></li>
      <li class="row good"><span class="rank">9</span><span class="store">(4) UyzYfIIMzU</span><span class="score">0.8</span></li>
      <li class="row good"><span class="rank">10</span><span class="store">(7) SCXulMdjcB</span><span class="score">1</span></li>
    </ol>
    <ol class="ranking">
      <li class="row bad"><span class="rank">96</span><span class="store">(5) gBeGhPqZNF</span><span class="score">9.7</span></li>
      <li class="row bad"><span class="rank">97</span><span class="store">(8) gGhhZFICHP</span><span class="score">9.7</span></li>
      <li class="row bad"><span class="rank">98</span><span class="store">(9) emavLKfhzN</span><span class="score">9.8</span></li>
      <li class="row bad"><span class="rank">99</span><span class="store">(7) PyuviZHBxH</span><span class="score">9.8</span></li>
      <li class="row bad"><span class="rank">100</span><span class="store">(5) LldsyctcWm</span><span class="score">9.9</span></li>
    </ol>
  </section>
</main>

<!-- ===== Desktop ===== -->
<main class="view view--desktop">
  <section class="card">
    <header class="card-head"><div class="card-icon" role="img" aria-label="Team goal icon"></div><div class="card-titles"><h2 class="card-title">Team</h2><p class="card-result">Your result: <strong>92.1 %</strong></p></div></header>
    <div class="goal"><span>Use Slow Stock wherever possible</span><span class="goal-target">80 %</span></div>
    <ol class="ranking">
      <li class="row bad"><span class="rank">1</span><span class="store">(1) yjcQbtCyQu</span><span class="score">1 %</span></li>
      <li class="row bad"><span class="rank">2</span><span class="store">(1) crsmicfXwS</span><span class="score">1 %</span></li>
      <li class="row bad"><span class="rank">3</span><span class="store">(2) wnLJojLRSf</span><span class="score">2 %</span></li>
      <li class="row bad"><span class="rank">4</span><span class="store">(2) swEbjeRrpi</span><span class="score">2 %</span></li>
      <li class="row bad"><span class="rank">5</span><span class="store">(4) oUauMPncOA</span><span class="score">4 %</span></li>
      <li class="row bad"><span class="rank">6</span><span class="store">(5) vYuFdHZExR</span><span class="score">5 %</span></li>
      <li class="row bad"><span class="rank">7</span><span class="store">(5) jvBnNaGkeE</span><span class="score">5 %</span></li>
      <li class="row bad"><span class="rank">8</span><span class="store">(6) CuWIivexCs</span><span class="score">6 %</span></li>
      <li class="row bad"><span class="rank">9</span><span class="store">(7) XQFCUbSoko</span><span class="score">7 %</span></li>
      <li class="row bad"><span class="rank">10</span><span class="store">(7) GucpFDVVJP</span><span class="score">7 %</span></li>
    </ol>
    <ol class="ranking">
      <li class="row good"><span class="rank">96</span><span class="store">(94) VaDGNkvwai</span><span class="score">94 %</span></li>
      <li class="row good"><span class="rank">97</span><span class="store">(94) IBjPTiBSlh</span><span class="score">94 %</span></li>
      <li class="row good"><span class="rank">98</span><span class="store">(96) iWwFhTvkZb</span><span class="score">96 %</span></li>
      <li class="row good"><span class="rank">99</span><span class="store">(96) IzLCIRKlLu</span><span class="score">96 %</span></li>
      <li class="row good"><span class="rank">100</span><span class="store">(96) pXPrzpcrUY</span><span class="score">96 %</span></li>
    </ol>
  </section>
  <section class="card">
    <header class="card-head"><div class="card-icon" role="img" aria-label="Slow stock goal icon"></div><div class="card-titles"><h2 class="card-title">Slow</h2><p class="card-result">Your result: <strong>0 %</strong></p></div></header>
    <div class="goal"><span>Less than 0% of inventory slower than 100 days</span><span class="goal-target">&lt; 1 %</span></div>
    <ol class="ranking">
      <li class="row good"><span class="rank">1</span><span class="store">(89) NZBGVulmnc</span><span class="score">0 %</span></li>
      <li class="row good"><span class="rank">2</span><span class="store">(80) GaccDehKUO</span><span class="score">0 %</span></li>
      <li class="row good"><span class="rank">3</span><span class="store">(55) aPfpNcqcDh</span><span class="score">0 %</span></li>
      <li class="row good"><span class="rank">4</span><span class="store">(97) YqyVfKITII</span><span class="score">0 %</span></li>
      <li class="row good"><span class="rank">5</span><span class="store">(67) PvQdqyeaHr</span><span class="score">0 %</span></li>
      <li class="row bad you"><span class="rank">6</span><span class="store">(00) Your Store</span><span class="score">2 %</span></li>
      <li class="row bad"><span class="rank">7</span><span class="store">(40) jyMfVYIVbl</span><span class="score">2 %</span></li>
      <li class="row bad"><span class="rank">8</span><span class="store">(11) QSESmpDJqw</span><span class="score">2 %</span></li>
      <li class="row bad"><span class="rank">9</span><span class="store">(71) nIlaXFpJWv</span><span class="score">2 %</span></li>
      <li class="row bad"><span class="rank">10</span><span class="store">(51) ENrkkveKpb</span><span class="score">2 %</span></li>
    </ol>
    <ol class="ranking">
      <li class="row bad"><span class="rank">96</span><span class="store">(90) VZgTUWgJTU</span><span class="score">8 %</span></li>
      <li class="row bad"><span class="rank">97</span><span class="store">(67) nRGVsKcZhP</span><span class="score">9 %</span></li>
      <li class="row bad"><span class="rank">98</span><span class="store">(32) JckeFPUVJV</span><span class="score">9 %</span></li>
      <li class="row bad"><span class="rank">99</span><span class="store">(57) RxygcFNCRC</span><span class="score">9 %</span></li>
      <li class="row bad"><span class="rank">100</span><span class="store">(20) MmydxeaOMu</span><span class="score">10 %</span></li>
    </ol>
  </section>
  <section class="card">
    <header class="card-head"><div class="card-icon" role="img" aria-label="Inventory turns goal icon"></div><div class="card-titles"><h2 class="card-title">Turns</h2><p class="card-result">Your result: <strong>2.2</strong></p></div></header>
    <div class="goal"><span>Turn inventory 6 or more times a year</span><span class="goal-target">&lt; 6</span></div>
    <ol class="ranking">
      <li class="row bad"><span class="rank">1</span><span class="store">(8) VZaEOSVkef</span><span class="score">0.2</span></li>
      <li class="row bad"><span class="rank">2</span><span class="store">(3) PcVKNpUNmj</span><span class="score">0.2</span></li>
      <li class="row bad"><span class="rank">3</span><span class="store">(4) RIlyRZsTln</span><span class="score">0.4</span></li>
      <li class="row bad"><span class="rank">4</span><span class="store">(9) epiNQFtERO</span><span class="score">0.6</span></li>
      <li class="row bad"><span class="rank">5</span><span class="store">(3) FbFOzkjSpF</span><span class="score">0.7</span></li>
      <li class="row bad"><span class="rank">6</span><span class="store">(7) RdzzkcVqtC</span><span class="score">0.8</span></li>
      <li class="row bad"><span class="rank">7</span><span class="store">(1) DiiIXiGkTx</span><span class="score">0.8</span></li>
      <li class="row bad"><span class="rank">8</span><span class="store">(1) jxWbwORyVa</span><span class="score">0.8</span></li>
      <li class="row bad"><span class="rank">9</span><span class="store">(4) UyzYfIIMzU</span><span class="score">0.8</span></li>
      <li class="row bad"><span class="rank">10</span><span class="store">(4) KVIgJQBgAc</span><span class="score">1</span></li>
    </ol>
    <ol class="ranking">
      <li class="row good"><span class="rank">96</span><span class="store">(5) gBeGhPqZNF</span><span class="score">9.7</span></li>
      <li class="row good"><span class="rank">97</span><span class="store">(8) gGhhZFICHP</span><span class="score">9.7</span></li>
      <li class="row good"><span class="rank">98</span><span class="store">(9) emavLKfhzN</span><span class="score">9.8</span></li>
      <li class="row good"><span class="rank">99</span><span class="store">(7) PyuviZHBxH</span><span class="score">9.8</span></li>
      <li class="row good"><span class="rank">100</span><span class="store">(5) LldsyctcWm</span><span class="score">9.9</span></li>
    </ol>
  </section>
  <section class="card">
    <header class="card-head"><div class="card-icon" role="img" aria-label="Inventory value goal icon"></div><div class="card-titles"><h2 class="card-title">Values</h2><p class="card-result">Your result: <strong>1.9</strong></p></div></header>
    <div class="goal"><span>Inventory Value to be around 1.25 x you last months INVENTORY sales</span><span class="goal-target">1.25</span></div>
    <ol class="ranking">
      <li class="row good"><span class="rank">1</span><span class="store">(8) VZaEOSVkef</span><span class="score">0.2</span></li>
      <li class="row good"><span class="rank">2</span><span class="store">(3) PcVKNpUNmj</span><span class="score">0.2</span></li>
      <li class="row good"><span class="rank">3</span><span class="store">(4) RIlyRZsTln</span><span class="score">0.4</span></li>
      <li class="row good"><span class="rank">4</span><span class="store">(9) epiNQFtERO</span><span class="score">0.6</span></li>
      <li class="row good"><span class="rank">5</span><span class="store">(3) FbFOzkjSpF</span><span class="score">0.7</span></li>
      <li class="row good"><span class="rank">6</span><span class="store">(7) RdzzkcVqtC</span><span class="score">0.8</span></li>
      <li class="row good"><span class="rank">7</span><span class="store">(1) DiiIXiGkTx</span><span class="score">0.8</span></li>
      <li class="row good"><span class="rank">8</span><span class="store">(1) jxWbwORyVa</span><span class="score">0.8</span></li>
      <li class="row good"><span class="rank">9</span><span class="store">(4) UyzYfIIMzU</span><span class="score">0.8</span></li>
      <li class="row good"><span class="rank">10</span><span class="store">(7) SCXulMdjcB</span><span class="score">1</span></li>
    </ol>
    <ol class="ranking">
      <li class="row bad"><span class="rank">96</span><span class="store">(5) gBeGhPqZNF</span><span class="score">9.7</span></li>
      <li class="row bad"><span class="rank">97</span><span class="store">(8) gGhhZFICHP</span><span class="score">9.7</span></li>
      <li class="row bad"><span class="rank">98</span><span class="store">(9) emavLKfhzN</span><span class="score">9.8</span></li>
      <li class="row bad"><span class="rank">99</span><span class="store">(7) PyuviZHBxH</span><span class="score">9.8</span></li>
      <li class="row bad"><span class="rank">100</span><span class="store">(5) LldsyctcWm</span><span class="score">9.9</span></li>
    </ol>
  </section>
</main>

</body>
</html>
```